Business card for auto dealership

Looking for a clean modern design.
Would like attached logo incorporated

Industry/Entity Type

Car dealership

Contact Information for Business Card

Name, website, phone, cell, fax, email

```html
<!DOCTYPE html>
<html lang="en">
<head>
<meta charset="utf-8">
<title>Brennan Truck &amp; Auto Sales – Business Card</title>
<link href="https://fonts.googleapis.com/css2?family=Montserrat:wght@400;700;800&display=swap" rel="stylesheet">
<style>
  :root{
    --page:#2a2a2a;
    --card:#151515;
    --card-edge:#0a0a0a;
    --ink:#ffffff;
    --ink-soft:#e6e6e6;
    --rule:#bdbdbd;
  }
  *{margin:0;padding:0;box-sizing:border-box}
  html,body{width:1200px;height:960px;overflow:hidden}
  body{
    background:var(--page);
    font-family:"Montserrat",Arial,sans-serif;
    display:flex;flex-direction:column;align-items:center;justify-content:center;gap:44px;
  }
  .card{
    width:700px;height:400px;
    background:linear-gradient(135deg,#222 0%,var(--card) 45%,#0f0f0f 100%);
    border-radius:4px;
    box-shadow:0 3px 0 var(--card-edge),0 6px 0 #050505,0 18px 30px rgba(0,0,0,.55);
    color:var(--ink);
    position:relative;
  }
  .card-front{display:flex;align-items:center;justify-content:center}
  .wordmark{text-align:center;font-weight:800;line-height:1}
  .wordmark-name{display:block;font-size:92px;letter-spacing:-1px}
  .wordmark-tag{display:block;font-size:26px;letter-spacing:2px;margin-top:6px}
  .card-back{display:flex;align-items:center;padding:0 56px 0 60px}
  .identity{width:300px;text-align:right}
  .identity .wordmark{text-align:left;margin-bottom:26px}
  .identity .wordmark-name{font-size:54px}
  .identity .wordmark-tag{font-size:15px;letter-spacing:1.2px;margin-top:4px}
  .person-name{font-size:26px;font-weight:700;letter-spacing:.5px}
  .person-role{font-size:16px;font-weight:400;color:var(--ink-soft);margin-top:4px}
  .divider{width:1px;height:170px;background:var(--rule);margin:0 34px 0 30px}
  .contact-list{list-style:none;font-size:19px;font-weight:400;color:var(--ink-soft)}
  .contact-list li{display:flex;align-items:center;gap:12px;height:32px;white-space:nowrap}
  .contact-list svg{width:18px;height:18px;fill:var(--ink);flex:none}
</style>
</head>
<body>

<section class="card card-front" aria-label="Business card front">
  <div class="wordmark">
    <span class="wordmark-name">Brennan</span>
    <span class="wordmark-tag">TRUCK &amp; AUTO SALES</span>
  </div>
</section>

<section class="card card-back" aria-label="Business card back">
  <div class="identity">
    <div class="wordmark">
      <span class="wordmark-name">Brennan</span>
      <span class="wordmark-tag">TRUCK &amp; AUTO SALES</span>
    </div>
    <p class="person-name">DANA BRENNAN</p>
    <p class="person-role">Owner</p>
  </div>

  <div class="divider"></div>

  <ul class="contact-list">
    <li>
      <svg viewBox="0 0 24 24" aria-hidden="true"><path d="M3 9c0-2 4-4 9-4s9 2 9 4v2h-5V9c-1-.6-2.5-1-4-1s-3 .4-4 1v2H3z"/><path d="M6 12h12l2 8H4z"/></svg>
      555-010-2387
    </li>
    <li>
      <svg viewBox="0 0 24 24" aria-hidden="true"><path d="M6.6 10.8a15 15 0 0 0 6.6 6.6l2.2-2.2c.3-.3.7-.4 1-.2 1.1.4 2.3.6 3.6.6.6 0 1 .4 1 1V20c0 .6-.4 1-1 1A17 17 0 0 1 3 4c0-.6.4-1 1-1h3.5c.6 0 1 .4 1 1 0 1.3.2 2.5.6 3.6.1.3 0 .7-.2 1z"/></svg>
      555-010-6952
    </li>
    <li>
      <svg viewBox="0 0 24 24" aria-hidden="true"><path d="M7 3h10v5H7z"/><path d="M4 9h16v9h-3v3H7v-3H4zm5 7v3h6v-3z"/></svg>
      555-010-3418
    </li>
    <li>
      <svg viewBox="0 0 24 24" aria-hidden="true"><path d="M2 5h20v14H2zm2 2v.5l8 5 8-5V7z"/></svg>
      dana@brennanauto.com
    </li>
    <li>
      <svg viewBox="0 0 24 24" aria-hidden="true"><circle cx="12" cy="12" r="10"/></svg>
      Brennanauto.com
    </li>
  </ul>
</section>

</body>
</html>
```